The Bridgewell Counseling Group - Practice Flyer

We need a flyer that generally advertises our services. I've uploaded one old flyer as well as examples of others. I like the style of the materials made by this practice: https://www.facebook.com/MarlowTherapyStudioNorth

```html
<!DOCTYPE html>
<html lang="en">
<head>
<meta charset="utf-8">
<title>The Bridgewell Counseling Group – Practice Flyer</title>
<link rel="stylesheet" href="https://fonts.googleapis.com/css2?family=Libre+Caslon+Text:wght@400;700&family=Montserrat:wght@400;500;600;700&display=swap">
<style>
  :root{
    --green:#97ad31;
    --green-logo:#2b3f25;
    --dark:#403b30;
    --ink:#2e2e2e;
    --grey-band:#ebebeb;
    --page-bg:#dedede;
    --white:#ffffff;
  }
  *{margin:0;padding:0;box-sizing:border-box}
  html,body{width:960px;height:1200px;overflow:hidden;background:var(--page-bg)}
  body{font-family:"Montserrat",sans-serif;color:var(--ink)}
  .flyer{position:absolute;left:56px;top:0;width:848px;height:1200px;background:var(--white);overflow:hidden}

  .brand{position:absolute;top:52px;left:0;width:100%;text-align:center;
    font-family:"Libre Caslon Text",serif;font-weight:700;color:var(--green-logo);
    font-size:34px;line-height:1.1;letter-spacing:.5px}
  .brand-mark{display:inline-block;width:14px;height:14px;background:var(--green-logo);margin-right:10px;vertical-align:middle}

  .hero{position:absolute;top:120px;left:0;width:100%;height:420px;
    background:linear-gradient(180deg,#ffffff 0%,#d9d6d1 14%,#8a8579 32%,#4b463b 55%,#3a342b 78%,#4a4238 100%)}
  .hero-title{position:absolute;top:340px;left:0;width:100%;text-align:center;
    font-family:"Libre Caslon Text",serif;font-weight:700;color:var(--white);
    font-size:63px;line-height:62px;letter-spacing:.5px}

  .rule{position:absolute;top:540px;left:0;width:100%;height:9px;background:var(--green)}
  .badge{position:absolute;top:512px;left:390px;width:68px;height:68px;border-radius:50%;
    background:var(--white);box-shadow:0 0 0 4px #f1f1f1}
  .badge svg{position:absolute;left:0;top:0}

  .about{position:absolute;left:59px;top:575px;width:338px;height:210px;background:var(--green);
    border-radius:10px 0 0 10px;padding:14px 22px 0 32px}
  .about h2{font-family:"Libre Caslon Text",serif;font-weight:700;font-size:25px;color:var(--dark);margin-bottom:10px;white-space:nowrap}
  .about p{font-size:10.6px;font-weight:700;line-height:13.7px;color:var(--white)}

  .intro{position:absolute;left:417px;top:577px;width:375px;font-size:9.4px;line-height:12px;color:#444}
  .conditions{position:absolute;top:624px;list-style:none;font-size:11px;font-weight:500;line-height:13.6px;letter-spacing:.2px;color:#333}
  .conditions li{position:relative;padding-left:21px;margin-bottom:6px}
  .conditions-a{left:416px;width:160px}
  .conditions-b{left:597px;width:200px;top:626px}
  .tick{position:absolute;left:0;top:1px;width:12px;height:12px}

  .science{position:absolute;left:59px;top:803px;width:730px;font-size:10.6px;line-height:13.8px;color:#444}

  .services{position:absolute;left:0;top:877px;width:100%;height:250px;background:var(--grey-band)}
  .services-banner{position:absolute;left:239px;top:862px;width:370px;height:46px}
  .services-banner h2{position:absolute;left:0;top:4px;width:100%;text-align:center;
    font-family:"Libre Caslon Text",serif;font-weight:400;font-size:31px;color:var(--white)}
  .service-list{position:absolute;list-style:none;font-size:11px;font-weight:700;letter-spacing:.3px;color:#333}
  .service-list li{position:relative;padding-left:25px;height:22.7px;line-height:13px}
  .service-list .tick{top:0}
  .services-a{left:62px;top:924px}
  .services-b{left:463px;top:927px}
  .services-b li.two{height:30px}
  .divider{position:absolute;left:431px;top:933px;width:0;height:124px;border-left:2px dotted #b5b5b5}

  .footer-dark{position:absolute;left:0;top:1158px;width:100%;height:42px;background:var(--dark)}
  .footer-green{position:absolute;left:0;top:1135px}
  .phone{position:absolute;left:60px;top:1136px;font-size:26px;font-weight:700;color:var(--white);letter-spacing:.3px}
  .site{position:absolute;left:60px;top:1172px;font-size:12.2px;font-weight:700;color:var(--white)}
  .phone svg,.site svg{vertical-align:middle;margin-right:5px}
  .find{position:absolute;left:375px;top:1171px;font-size:12px;font-weight:700;color:var(--white)}
  .social{position:absolute;top:1169px;width:18px;height:18px;border-radius:50%;background:var(--white)}
  .sep{position:absolute;left:562px;top:1166px;width:1px;height:22px;background:#8a8577}
  .credit{position:absolute;left:575px;top:1170px;font-size:6.2px;line-height:8px;color:#e8e8e8}
  .credit b{font-weight:700}
</style>
</head>
<body>
<div class="flyer">
  <svg width="0" height="0" style="position:absolute">
    <defs>
      <symbol id="tick" viewBox="0 0 12 12">
        <circle cx="6" cy="6" r="6" fill="#3a3a3a"/>
        <path d="M3.3 6.2l1.8 1.8 3.6-3.7" fill="none" stroke="#fff" stroke-width="1.5" stroke-linecap="round" stroke-linejoin="round"/>
      </symbol>
    </defs>
  </svg>

  <div class="hero" role="img" aria-label="Photograph of a misty mountain lake with forested slopes, a small canoe and rocks in the foreground"></div>

  <div class="brand"><span class="brand-mark"></span>The Bridgewell Counseling Group</div>

  <h1 class="hero-title">THE BRIDGEWELL<br>COUNSELING GROUP</h1>

  <div class="rule"></div>
  <div class="badge">
    <svg width="68" height="68" viewBox="0 0 68 68"><circle cx="34" cy="34" r="13" fill="#7fa83a"/></svg>
  </div>

  <section class="about">
    <h2>Expertise Within Reach</h2>
    <p>The Bridgewell Counseling Group (BCG) is a multi-site, outpatient behavioral healthcare provider specializing in the evaluation and evidence-based treatment of anxiety disorders, obsessive-compulsive and related disorders, and neurodevelopmental disorders. With locations in New Jersey and telehealth services available across the United States, BCG's nationally renowned team provides excellence in individualized care.</p>
  </section>

  <p class="intro">Hope starts here. At BCG, we see treatment successes every day – We see people learn to overcome their fears, drop their struggles, and reconnect with what matters most to them. We see people get their lives back.</p>

  <ul class="conditions conditions-a">
    <li><svg class="tick"><use href="#tick"/></svg>Anxiety and Panic Disorders</li>
    <li><svg class="tick"><use href="#tick"/></svg>Phobias</li>
    <li><svg class="tick"><use href="#tick"/></svg>Posttraumatic Stress Disorder</li>
    <li><svg class="tick"><use href="#tick"/></svg>Obsessive-Compulsive Disorder</li>
    <li><svg class="tick"><use href="#tick"/></svg>Trichotillomania, Excoriation Disorder, and other BFRBs</li>
  </ul>
  <ul class="conditions conditions-b">
    <li><svg class="tick"><use href="#tick"/></svg>Body Dysmorphic Disorder</li>
    <li><svg class="tick"><use href="#tick"/></svg>Hoarding Disorder</li>
    <li><svg class="tick"><use href="#tick"/></svg>Tic and Tourette's Disorders</li>
    <li><svg class="tick"><use href="#tick"/></svg>Attention-Deficit / Hyperactivity Disorder</li>
    <li style="margin-top:10px"><svg class="tick"><use href="#tick"/></svg>Learning Disorders</li>
    <li style="margin-top:10px"><svg class="tick"><use href="#tick"/></svg>Disruptive Behavior Disorders</li>
  </ul>

  <p class="science">We value science. We do what works, based on the best available research and scientific evidence, ensuring you receive exceptional care. Beyond the office, BCG clinicians are leaders in the field, providing training and consultation to clinicians and educators around the country.</p>

  <div class="services"></div>
  <div class="services-banner">
    <svg width="370" height="46" viewBox="0 0 370 46">
      <path d="M0 4 Q10 0 22 2 L22 16 Z" fill="#2a2720"/>
      <path d="M370 4 Q360 0 348 2 L348 16 Z" fill="#2a2720"/>
      <path d="M22 2 H348 V34 Q348 46 336 46 H34 Q22 46 22 34 Z" fill="var(--dark)"/>
    </svg>
    <h2>Services We Provide</h2>
  </div>

  <ul class="service-list services-a">
    <li><svg class="tick"><use href="#tick"/></svg>Cognitive Behavioral Therapy</li>
    <li><svg class="tick"><use href="#tick"/></svg>Exposure and Response Prevention</li>
    <li><svg class="tick"><use href="#tick"/></svg>Prolonged Exposure</li>
    <li><svg class="tick"><use href="#tick"/></svg>Cognitive Processing Therapy</li>
    <li><svg class="tick"><use href="#tick"/></svg>Acceptance and Commitment Therapy</li>
    <li><svg class="tick"><use href="#tick"/></svg>Comprehensive Behavioral Intervention for Tics</li>
    <li><svg class="tick"><use href="#tick"/></svg>Cognitive Behavioral Therapy for Insomnia</li>
    <li><svg class="tick"><use href="#tick"/></svg>Parent-Child Interaction Therapy</li>
    <li><svg class="tick"><use href="#tick"/></svg>Supportive Parenting for Anxious Childhood Emotions</li>
  </ul>
  <div class="divider"></div>
  <ul class="service-list services-b">
    <li><svg class="tick"><use href="#tick"/></svg>Organizational Skills Training</li>
    <li><svg class="tick"><use href="#tick"/></svg>Parent Management Training</li>
    <li><svg class="tick"><use href="#tick"/></svg>Parent-Child Interaction Therapy</li>
    <li><svg class="tick"><use href="#tick"/></svg>Emotionally Focused Therapy</li>
    <li><svg class="tick"><use href="#tick"/></svg>Psychodynamic and Interpersonal Therapy</li>
    <li class="two"><svg class="tick"><use href="#tick"/></svg>Psychological, Psychoeducational, and<br>Forensic Assessment</li>
  </ul>

  <div class="footer-dark"></div>
  <svg class="footer-green" width="380" height="65" viewBox="0 0 380 65">
    <path d="M0 0 H330 Q340 0 344 8 L378 65 H0 Z" fill="var(--green)"/>
    <path d="M330 0 Q340 0 344 8 L378 65" fill="none" stroke="#ffffff" stroke-width="2"/>
  </svg>
  <div class="phone"><svg width="16" height="16" viewBox="0 0 16 16"><path d="M3 1.5l2.5-.5 1.5 3.5-1.8 1.2a9 9 0 004.1 4.1L10.5 8l3.5 1.5-.5 2.5c-.3 1.3-1.6 2.2-3 1.9C5.8 13 3 10.2 2.1 5.5 1.8 4.1 2 2 3 1.5z" fill="#fff"/></svg>(555) 014-2837</div>
  <div class="site"><svg width="13" height="13" viewBox="0 0 14 14"><circle cx="7" cy="7" r="6" fill="none" stroke="#fff" stroke-width="1.4"/><path d="M1 7h12M7 1c-3 3.5-3 8.5 0 12M7 1c3 3.5 3 8.5 0 12" fill="none" stroke="#fff" stroke-width="1.1"/></svg>BridgewellCounselingGroup.com</div>

  <div class="find">Find us on</div>
  <span class="social" style="left:450px"></span>
  <span class="social" style="left:469px"></span>
  <span class="social" style="left:488px"></span>
  <span class="social" style="left:507px"></span>
  <div class="sep"></div>
  <p class="credit">Elena R. Castell, PsyD. Licensed Psychologist,<br>Executive Director, <b>Lic. No. 35SI00912400</b></p>
</div>
</body>
</html>
```